VelnoriCore Business Cards

Will need a front and back design for a business card for VelnoriCore.
Can accept the final product as an illustrator file.
www.velnoricore-example.com is the company website.

Target Market(s)

he target market are Chief Technology Officers and people in the tech field.

Industry/Entity Type

Business

Requirements
Must have
• - The business card must have on one of the sides
name
title
company
phone
email
website
The other side may be of some design, derivation of logo and or colors

```html
<!DOCTYPE html>
<html lang="en">
<head>
<meta charset="utf-8">
<title>VelnoriCore Business Cards</title>
<link rel="stylesheet" href="https://fonts.googleapis.com/css2?family=Montserrat:wght@600;700;800&display=swap">
<style>
  :root {
    --bg: #e6e7e9;
    --card-white: #f7f7f8;
    --card-grey: #dcdde0;
    --navy: #1b2f7e;
    --navy-deep: #0f1d5c;
    --blue: #1f4aa8;
    --blue-light: #3a6fd0;
    --grey-text: #9a9ca2;
    --white: #ffffff;
  }
  * { margin: 0; padding: 0; box-sizing: border-box; }
  html, body { width: 1067px; height: 1200px; overflow: hidden; }
  body {
    background: var(--bg);
    font-family: "Montserrat", Arial, sans-serif;
    position: relative;
  }
  .card {
    position: absolute;
    left: 123px;
    width: 820px;
    height: 470px;
    border-radius: 28px;
    overflow: hidden;
    box-shadow: 0 10px 30px rgba(0,0,0,.18);
  }
  .card--front { top: 90px; }
  .card--back { top: 640px; }

  .card-surface {
    position: absolute; inset: 0;
    background: radial-gradient(ellipse at 50% 40%, var(--card-white) 0%, var(--card-grey) 100%);
  }

  /* Brand lockup */
  .brand { position: absolute; display: flex; flex-direction: column; align-items: center; }
  .brand-mark {
    border-radius: 50%;
    background: var(--navy);
  }
  .brand-name {
    color: var(--navy);
    font-weight: 800;
    letter-spacing: 0.5px;
    line-height: 1;
  }
  .brand-tagline {
    color: var(--grey-text);
    font-weight: 600;
    text-transform: uppercase;
    letter-spacing: 2px;
  }

  .card--front .brand { left: 0; right: 0; top: 80px; }
  .card--front .brand-mark { width: 150px; height: 150px; margin-bottom: 28px; }
  .card--front .brand-name { font-size: 48px; }
  .card--front .brand-tagline { font-size: 15px; margin-top: 6px; }
  .front-website {
    position: absolute; left: 0; right: 0; top: 385px;
    text-align: center;
    color: var(--navy);
    font-size: 17px; font-weight: 700; letter-spacing: 2px;
  }

  .card--back .brand { left: 30px; width: 300px; top: 120px; }
  .card--back .brand-mark { width: 125px; height: 125px; margin-bottom: 26px; }
  .card--back .brand-name { font-size: 30px; }
  .card--back .brand-tagline { font-size: 10px; margin-top: 5px; letter-spacing: 1.5px; }

  .back-panel { position: absolute; inset: 0; width: 820px; height: 470px; }

  .contact {
    position: absolute; left: 440px; top: 55px;
    color: var(--white);
  }
  .contact-name { font-size: 26px; font-weight: 700; }
  .contact-title { font-size: 15px; font-weight: 600; margin-top: 2px; }
  .contact-company { font-size: 24px; font-weight: 700; margin-top: 30px; }
  .contact-tagline { font-size: 15px; font-weight: 600; }
  .contact-address { font-size: 17px; font-weight: 600; margin-top: 28px; line-height: 1.3; }
  .contact-lines { list-style: none; margin-top: 28px; }
  .contact-lines li {
    display: flex; align-items: center; gap: 14px;
    font-size: 17px; font-weight: 600; margin-bottom: 10px;
  }
  .contact-lines svg { width: 20px; height: 20px; flex: none; }
</style>
</head>
<body>

  <section class="card card--front" aria-label="Card front">
    <div class="card-surface" role="img" aria-label="Soft grey hexagon texture background"></div>
    <div class="brand">
      <div class="brand-mark"></div>
      <div class="brand-name">VelnoriCore</div>
      <div class="brand-tagline">Guarding Every Network</div>
    </div>
    <div class="front-website">www.velnoricore-example.com</div>
  </section>

  <section class="card card--back" aria-label="Card back">
    <div class="card-surface" role="img" aria-label="Soft grey hexagon texture background"></div>
    <svg class="back-panel" viewBox="0 0 820 470" aria-hidden="true">
      <defs>
        <linearGradient id="panelBlue" x1="0" y1="0" x2="1" y2="1">
          <stop offset="0" stop-color="#2348a6"/>
          <stop offset="1" stop-color="#0f1d5c"/>
        </linearGradient>
      </defs>
      <path d="M335 0 C 255 130 262 350 372 470 L 820 470 L 820 0 Z" fill="#3a6fd0"/>
      <path d="M358 0 C 282 130 290 350 398 470 L 820 470 L 820 0 Z" fill="#ffffff"/>
      <path d="M366 0 C 292 130 300 350 408 470 L 820 470 L 820 0 Z" fill="url(#panelBlue)"/>
    </svg>
    <div class="brand">
      <div class="brand-mark"></div>
      <div class="brand-name">VelnoriCore</div>
      <div class="brand-tagline">Guarding Every Network</div>
    </div>
    <div class="contact">
      <div class="contact-name">Dara Whitfield</div>
      <div class="contact-title">Manager</div>
      <div class="contact-company">VelnoriCore</div>
      <div class="contact-tagline">Guarding Every Network</div>
      <div class="contact-address">218 Halvern Street<br>Brookton NY 10450</div>
      <ul class="contact-lines">
        <li>
          <svg viewBox="0 0 24 24" fill="#ffffff"><path d="M6.6 10.8a15.1 15.1 0 0 0 6.6 6.6l2.2-2.2a1 1 0 0 1 1-.25 11.4 11.4 0 0 0 3.6.57 1 1 0 0 1 1 1V20a1 1 0 0 1-1 1A17 17 0 0 1 3 4a1 1 0 0 1 1-1h3.5a1 1 0 0 1 1 1c0 1.250.2 2.450.57 3.6a1 1 0 0 1-.25 1z"/></svg>
          (555) 014-2290
        </li>
        <li>
          <svg viewBox="0 0 24 24" fill="none" stroke="#ffffff" stroke-width="2"><rect x="3" y="5" width="18" height="14" rx="1"/><path d="M3 6l9 7 9-7"/></svg>
          info@velnoricore-example.com
        </li>
        <li>
          <svg viewBox="0 0 24 24" fill="none" stroke="#ffffff" stroke-width="2"><circle cx="12" cy="12" r="9"/><path d="M3 12h18M12 3c3 3 3 15 0 18M12 3c-3 3-3 15 0 18"/></svg>
          www.velnoricore-example.com
        </li>
      </ul>
    </div>
  </section>

</body>
</html>
```